QBTx 500mg CBD Tincture

We are rebranding and need new label ideas. I’m including our old label as reference to the bottle and the die lines.
Our company is called Marlow Fiber Company and we are a CBD company.

We would like a design for 1oz tincture bottle with a dropper. They are matte white with white tops. We have 2 flavors, peppermint and orange cream

I’ve uploaded the logo, colors and theme of the rebranding. We only want to use the Logos, no writing out of the company name. We are trying to shift to QBTx so that we can market more through the whole country.

We like clean and neat design. Elegant meets modern. Not cluttered. Our logo is new too so you can use that as an idea.

Requirements
Must have
• A neat and clean design. Something that is easily duplicated over other products over time.
Should not have
• My pro just must not have the company name written out. Only logo. No cannabis leaves.

```html
<!DOCTYPE html>
<html lang="en">
<head>
<meta charset="utf-8">
<title>QBTx CBD Oil Labels</title>
<link rel="stylesheet" href="https://fonts.googleapis.com/css2?family=Alfa+Slab+One&family=Parisienne&family=Quicksand:wght@400;500&display=swap">
<style>
  :root {
    --page: #ffffff;
    --label: #fbfbfb;
    --label-edge: #dcdcdc;
    --ink: #1a1a1a;
    --orange: #f4a47d;
    --orange-deep: #c86b40;
    --teal: #80c4be;
    --teal-deep: #3e8b87;
    --muted: #a8a8a8;
  }
  * { box-sizing: border-box; margin: 0; padding: 0; }
  html, body { width: 1200px; height: 947px; overflow: hidden; background: var(--page); }
  .canvas { position: relative; width: 1200px; height: 947px; }
  .label {
    position: absolute; top: 166px; width: 436px; height: 615px;
    background: linear-gradient(90deg, #e9e9e9 0%, var(--label) 8%, var(--label) 92%, #e4e4e4 100%);
    border: 1px solid var(--label-edge);
    text-align: center;
    font-family: "Quicksand", sans-serif;
  }
  .label--orange { left: 142px; --accent: var(--orange); --accent-deep: var(--orange-deep); }
  .label--mint { left: 622px; --accent: var(--teal); --accent-deep: var(--teal-deep); }
  .brand {
    position: absolute; left: 130px; top: 28px; width: 176px; height: 176px;
    border: 1.5px solid var(--ink); border-radius: 50%;
    display: flex; align-items: center; justify-content: center;
  }
  .brand-name { font-family: "Quicksand", sans-serif; font-weight: 500; font-size: 40px; color: var(--ink); }
  .flavor {
    position: absolute; left: 0; right: 0; top: 222px;
    font-family: "Parisienne", cursive; font-size: 56px; line-height: 1; color: var(--accent);
  }
  .product-box {
    position: absolute; left: 35px; top: 302px; width: 366px; height: 106px;
    background: var(--accent); padding: 10px;
  }
  .product-box-inner {
    width: 100%; height: 100%; border: 2px solid rgba(255,255,255,0.85);
    display: flex; align-items: center; justify-content: center;
    font-family: "Alfa Slab One", serif; font-size: 62px; color: #fff; letter-spacing: 1px;
  }
  .strength {
    position: absolute; left: 0; right: 0; top: 414px;
    font-family: "Alfa Slab One", serif; font-size: 38px; color: var(--accent); word-spacing: 14px;
  }
  .spectrum {
    position: absolute; left: 0; right: 0; top: 500px;
    font-size: 36px; color: var(--accent-deep); letter-spacing: 0.5px;
  }
  .volume {
    position: absolute; left: 0; right: 0; top: 580px;
    font-size: 21px; color: var(--muted);
  }
</style>
</head>
<body>
<main class="canvas">
  <section class="label label--orange">
    <div class="brand"><span class="brand-name">QBTx</span></div>
    <p class="flavor">Orange Cream</p>
    <div class="product-box"><div class="product-box-inner">CBD OIL</div></div>
    <p class="strength">500 MG</p>
    <p class="spectrum">BROAD SPECTRUM</p>
    <p class="volume">1 OZ / 30 ml</p>
  </section>
  <section class="label label--mint">
    <div class="brand"><span class="brand-name">QBTx</span></div>
    <p class="flavor">Peppermint</p>
    <div class="product-box"><div class="product-box-inner">CBD OIL</div></div>
    <p class="strength">500 MG</p>
    <p class="spectrum">BROAD SPECTRUM</p>
    <p class="volume">1 OZ / 30 ml</p>
  </section>
</main>
</body>
</html>
```